POSTER FOR NEW MUSIC-THEATRE PRODUCTION - De Moerbeiwerkplaats

For our new theatre production 'Glasbroeder' we're looking for a new poster design.

All details can be found in the itinerary in attachment.
Updates

Dear designers

Thanks for some really good designs up to now.
Detailed feedback will follow from next week onwards since Im abroad for business and since I have very little internet access.

kind regards
Joris Meul

Target Market(s)

Theatres throughout Flanders (Belgium) when on tour in 2010-2011-2012. (expecting 70 performances)
Age is 14 up till 88 years old.

Requirements
Must have
• see itinerary in attachment
Nice to have
• Take a look to the poster design of our former production. We kind of liked the 'cool' look.
• Mind : use the new logo in attachment
Should not have
• too many colours.

```html
<!DOCTYPE html>
<html lang="nl">
<head>
<meta charset="utf-8">
<title>Glasbroeder – De Moerbeiwerkplaats</title>
<link href="https://fonts.googleapis.com/css2?family=Barlow:wght@400;600&family=Great+Vibes&display=swap" rel="stylesheet">
<style>
  :root {
    --ink: #000000;
    --paper: #ffffff;
    --accent: #e0197d;
    --ember: #e4572e;
    --muted: #3a3a3a;
  }
  * { box-sizing: border-box; margin: 0; padding: 0; }
  html, body { width: 849px; height: 1200px; overflow: hidden; background: var(--ink); }
  .poster {
    position: relative; width: 849px; height: 1200px; overflow: hidden;
    background: var(--ink); color: var(--paper);
    font-family: "Barlow", Arial, sans-serif;
  }
  .wing-photo {
    position: absolute; left: 0; top: 0; width: 849px; height: 560px;
    background:
      radial-gradient(ellipse 62% 55% at 48% 30%, #e8e8e8 0%, #a8a8a8 35%, #4a4a4a 65%, rgba(0,0,0,0) 85%),
      var(--ink);
  }
  .presenter {
    position: absolute; left: 363px; top: 572px;
    font-size: 23px; font-weight: 400; letter-spacing: 0.2px;
  }
  .title {
    position: absolute; left: 205px; top: 585px;
    font-family: "Great Vibes", cursive; font-size: 142px; line-height: 1;
    color: var(--accent); font-weight: 400;
  }
  .credits {
    position: absolute; left: 363px; top: 782px;
    font-size: 13px; line-height: 17.6px; list-style: none;
  }
  .credits li { display: flex; }
  .credits .role {
    width: 120px; display: flex; color: var(--accent);
    font-family: "Great Vibes", cursive; font-size: 15px;
  }
  .credits .role::after {
    content: ""; flex: 1; border-bottom: 1px dotted var(--accent);
    margin: 0 4px 5px 3px;
  }
  .credits .names { width: 220px; }
  .brand-name {
    position: absolute; left: 74px; top: 1086px;
    transform: rotate(-90deg); transform-origin: left top;
    font-size: 17px; font-weight: 600; letter-spacing: 0.5px;
    text-transform: uppercase; color: var(--paper); white-space: nowrap;
  }
  .brand-name .lead { text-transform: none; }
  .brand-dot {
    position: absolute; left: 62px; top: 1118px; width: 34px; height: 34px;
    border-radius: 50%; background: var(--ember);
  }
  .partners {
    position: absolute; left: 363px; top: 1110px; width: 231px; height: 40px;
    background: var(--paper); display: flex; align-items: center; gap: 6px; padding: 4px;
  }
  .partners span { display: block; height: 32px; background: #cfcfcf; }
  .partners .p1 { width: 40px; }
  .partners .p2 { flex: 1; }
  .partners .p3 { width: 32px; background: #d0282e; }
  .partners-note {
    position: absolute; left: 363px; top: 1153px; width: 231px;
    font-size: 5.5px; color: var(--paper);
  }
  .imprint {
    position: absolute; left: 840px; top: 1170px;
    transform: rotate(-90deg); transform-origin: left top;
    font-size: 5.5px; color: var(--muted); white-space: nowrap;
  }
</style>
</head>
<body>
<main class="poster">
  <div class="wing-photo" role="img" aria-label="Black-and-white photograph of white swan feathers on a black background"></div>

  <p class="presenter">de Moerbeiwerkplaats speelt</p>
  <h1 class="title">Glasbroeder</h1>

  <ul class="credits">
    <li><span class="role">Tekst</span><span class="names">Anke Verhulst</span></li>
    <li><span class="role">Regie</span><span class="names">Pieter Van Loock</span></li>
    <li><span class="role">Animatie</span><span class="names">Bram Nuyttens</span></li>
    <li><span class="role">Kostuumontwerp</span><span class="names">Sofie Desmedt</span></li>
    <li><span class="role">Lichtontwerp</span><span class="names">Koen Vermeiren Dewaele</span></li>
    <li><span class="role">Muziek &amp; Spel</span><span class="names">Jonas Verstraete, Lukas Verstraete, Matthias Verstraete, Dirk Lemmens, Joris Meul</span></li>
  </ul>

  <p class="brand-name"><span class="lead">de </span>Moerbeiwerkplaats</p>
  <div class="brand-dot"></div>

  <div class="partners" aria-label="Partners">
    <span class="p1"></span><span class="p2"></span><span class="p3"></span>
  </div>
  <p class="partners-note">Met de steun van het district en cultuurcentrum</p>

  <p class="imprint">V.U.: Moerbeiwerkplaats vzw, Joris Meul, Glasbroeder, Werkplaatsstraat 12, 2018 Antwerpen</p>
</main>
</body>
</html>
```